" Window Blinds and Shutters Business Card Design"

We require a business card design for a new windows blinds and shutters company based in Sydney.
The business name is 'Harbourlight Blinds and Shutters'.
We supply and install homes and businesses with internal and external window furnishings and finishes. This includes varieties of window blinds and window shutters.

Benefits of Harbourlight Blinds and Shutters :
Added security and privacy,
The ability to control the amount of sunlight,
Regulate internal temperature.

Blinds varieties:
Roller Blinds, Double Roller Blinds, Roman Blinds, Vertical Blinds, Aluminium venetians, Timber venetians and PVC Venetians.

Shutters varieties:
Plantation Shutters, Aluminium Louvre Shutters, Roller Shutters and Security Shutters .

Hi Designers,

Please have a look at my Business card design brief. I need your help to start my new business.

Thanks,

Daniel.

Reason: not 100% happy with the options available, close to 90% happy, need a little more refinement. Thank You & Good Luck

Target Market(s)

Home owners, business owners, shift workers , and new home builders.

Industry/Entity Type

Security

Contact Information for Business Card

Harbourlight Blinds and Shutters,

Daniel Brostow mobile: 0417586204,
Corey Wendt mobile: 0419248653,

email: daniel.brostow@mailvista.net
web: harbourlightblindsandshutters.com.au

Colors
ffffff
9d9d9d
f78f20

Requirements
Must have
• ON FRONT OF CARD
I have attached a picture of logo and need a designer to design a font logo for Harbourlight Blinds and Shutters similar, or open to suggestions.

FRONT OF CARD
Company message/:
"Framing every window with care"

BACK OF CARD
'For a FREE measure & quote call Daniel - 0417586204"
Nice to have
• Elegant yet professional.

Soft colours appealing to both male & female clients.

Should not have

• Unprofessional fonts

```html
<!DOCTYPE html>
<html lang="en">
<head>
<meta charset="utf-8">
<title>Harbourlight Blinds and Shutters — Business Card</title>
<link rel="stylesheet" href="https://fonts.googleapis.com/css2?family=Quicksand:wght@400;500&display=swap">
<style>
  :root {
    --stage: #5b4c45;
    --white: #ffffff;
    --teal: #3fd3cd;
    --ink: #111a1a;
    --rule: #e8eeee;
    --grey: #9d9d9d;
    --pale: #f6f9f9;
    --mist: #d8e9e9;
  }
  * { box-sizing: border-box; margin: 0; padding: 0; }
  html, body { width: 960px; height: 1200px; overflow: hidden; }
  body {
    background: var(--stage);
    font-family: "Quicksand", sans-serif;
    position: relative;
  }

  .brand-name { font-family: "Quicksand", sans-serif; font-weight: 500; line-height: 1.1; white-space: nowrap; }

  /* Brand presentation */
  .brand-hero {
    position: absolute; left: 0; top: 0; width: 960px; height: 380px;
    display: flex; flex-direction: column; align-items: center;
    color: var(--white);
  }
  .brand-hero .mark-dot {
    width: 130px; height: 130px; border-radius: 50%;
    background: var(--white); opacity: 0.9; margin-top: 52px;
  }
  .brand-hero .brand-name { font-size: 42px; margin-top: 40px; color: var(--white); }
  .brand-hero .brand-rule { width: 440px; height: 2px; background: var(--white); margin-top: 18px; }
  .brand-hero .tagline { font-size: 19px; font-weight: 500; margin-top: 12px; text-transform: uppercase; }

  /* Cards */
  .card { position: absolute; left: 158px; width: 668px; height: 382px; overflow: hidden; }

  .card-back { top: 396px; background: var(--ink); }
  .card-back .header {
    height: 114px; background: var(--white);
    display: flex; align-items: center; gap: 14px; padding-left: 20px;
  }
  .card-back .header .mark-dot { width: 58px; height: 58px; border-radius: 50%; background: var(--teal); flex: none; }
  .card-back .header .brand-name { color: var(--teal); font-size: 24px; }
  .card-back .header .mini-rule { width: 300px; height: 1px; background: var(--teal); margin: 6px 0 4px; }
  .card-back .header .mini-tag { font-size: 10px; color: var(--teal); text-transform: uppercase; }

  .contacts { position: absolute; left: 24px; top: 130px; width: 214px; color: var(--white); }
  .contact-name { font-size: 18px; }
  .contact-phone { font-size: 15px; display: flex; align-items: center; gap: 9px; margin: 6px 0 12px 2px; }
  .contact-phone svg { width: 13px; height: 13px; fill: var(--white); }
  .contacts .divider { height: 1px; background: var(--rule); margin-top: 8px; }
  .contact-email { font-size: 14px; margin-top: 10px; }

  .benefits { position: absolute; left: 277px; top: 130px; width: 380px; color: var(--white); }
  .benefits h2 { font-size: 18px; font-weight: 400; padding-bottom: 5px; border-bottom: 1px solid var(--rule); }
  .benefits ul { list-style: none; margin-top: 6px; }
  .benefits li { font-size: 16px; display: flex; align-items: center; gap: 6px; margin-bottom: 7px; }
  .benefits li svg { width: 15px; height: 15px; }

  .call-band {
    position: absolute; left: 12px; right: 12px; top: 294px; height: 38px;
    border-top: 1px solid var(--rule); border-bottom: 1px solid var(--rule);
    color: var(--white); font-size: 24px; font-weight: 500;
    display: flex; align-items: center; text-transform: uppercase;
  }
  .website { position: absolute; left: 12px; top: 344px; color: var(--white); font-size: 23px; }
  .website .url { font-style: italic; }

  .card-front {
    top: 798px;
    background: radial-gradient(ellipse at 50% 45%, var(--pale) 0%, var(--mist) 100%);
    display: flex; flex-direction: column; align-items: center;
  }
  .card-front .mark-dot {
    width: 96px; height: 96px; border-radius: 50%; background: var(--teal); margin-top: 72px;
  }
  .card-front .brand-name { color: var(--teal); font-size: 30px; margin-top: 34px; }
  .card-front .brand-rule { width: 290px; height: 1px; background: var(--teal); margin-top: 12px; }
  .card-front .tagline { font-size: 12px; color: var(--teal); margin-top: 8px; text-transform: uppercase; }
</style>
</head>
<body>

  <header class="brand-hero">
    <div class="mark-dot"></div>
    <h1 class="brand-name">Harbourlight Blinds and Shutters</h1>
    <div class="brand-rule"></div>
    <p class="tagline">Framing every window with care</p>
  </header>

  <section class="card card-back">
    <div class="header">
      <div class="mark-dot"></div>
      <div>
        <div class="brand-name">Harbourlight Blinds and Shutters</div>
        <div class="mini-rule"></div>
        <div class="mini-tag">Framing every window with care</div>
      </div>
    </div>

    <div class="contacts">
      <p class="contact-name">Daniel Brostow</p>
      <p class="contact-phone"><svg viewBox="0 0 24 24"><path d="M6.6 10.8c1.4 2.8 3.8 5.1 6.6 6.6l2.2-2.2c.3-.3.7-.4 1-.2 1.1.4 2.3.6 3.6.6.6 0 1 .4 1 1V20c0 .6-.4 1-1 1C10.6 21 3 13.4 3 4c0-.6.4-1 1-1h3.5c.6 0 1 .4 1 1 0 1.3.2 2.5.6 3.6.1.3 0 .7-.2 1z"/></svg>0417586204</p>
      <p class="contact-name">Corey Wendt</p>
      <p class="contact-phone"><svg viewBox="0 0 24 24"><path d="M6.6 10.8c1.4 2.8 3.8 5.1 6.6 6.6l2.2-2.2c.3-.3.7-.4 1-.2 1.1.4 2.3.6 3.6.6.6 0 1 .4 1 1V20c0 .6-.4 1-1 1C10.6 21 3 13.4 3 4c0-.6.4-1 1-1h3.5c.6 0 1 .4 1 1 0 1.3.2 2.5.6 3.6.1.3 0 .7-.2 1z"/></svg>0419248653</p>
      <div class="divider"></div>
      <p class="contact-email">daniel.brostow@mailvista.net</p>
    </div>

    <div class="benefits">
      <h2>Benefits of Harbourlight Blinds and Shutters</h2>
      <ul>
        <li><svg viewBox="0 0 16 16"><rect x="1" y="3" width="11" height="11" fill="none" stroke="#fff" stroke-width="1.3"/><path d="M3.5 8.5l3 3L14.5 2" fill="none" stroke="#fff" stroke-width="1.8"/></svg>Added security and privacy</li>
        <li><svg viewBox="0 0 16 16"><rect x="1" y="3" width="11" height="11" fill="none" stroke="#fff" stroke-width="1.3"/><path d="M3.5 8.5l3 3L14.5 2" fill="none" stroke="#fff" stroke-width="1.8"/></svg>The ability to control the amount of sunlight</li>
        <li><svg viewBox="0 0 16 16"><rect x="1" y="3" width="11" height="11" fill="none" stroke="#fff" stroke-width="1.3"/><path d="M3.5 8.5l3 3L14.5 2" fill="none" stroke="#fff" stroke-width="1.8"/></svg>Regulate internal temperature</li>
      </ul>
    </div>

    <p class="call-band">Call 0417586204 for a free measure and quote</p>
    <p class="website">Visit our website: <span class="url">harbourlightblindsandshutters.com.au</span></p>
  </section>

  <section class="card card-front">
    <div class="mark-dot"></div>
    <h2 class="brand-name">Harbourlight Blinds and Shutters</h2>
    <div class="brand-rule"></div>
    <p class="tagline">Framing every window with care</p>
  </section>

</body>
</html>
```